Weight loss surgery restaurant card

We need to create a card for patients who have undergone weight loss surgery to take to restaurants so they can request smaller meals. These patients have had surgery on their stomach so that they can only consume half to one cup of food at a time. So normal sized restaurant meals are way too big (and cost a lot). This card they can present to the restaurant to communicate the fact that they have had weight loss surgery and therefore request a smaller meal portion at reduced cost

Target Market(s)

Restaurants serving weight loss surgery patients

Industry/Entity Type

Health Care

Contact Information for Business Card

This will be a plastic card similar to business card size.

Requirements
Must have
• The front of the card should include the following text:
• The individual bearing this card has undergone weight loss surgery.
• This surgery restricts portion sizes to between half and one cup of food at a time.
• Please give consideration to allowing smaller portions of your regular meals to be ordered to reduce wastage and excess costs.
• Example: a half size portion priced at two thirds of usual cost.
• The back of the card will have spaces for the person to write certain information. These are the categories that can be filled in by hand:
• Name:
• Procedure performed:
• Date of procedure (month/year):
• Treating Clinic Name:
• Treating Clinic Signature:
• Somewhere down the bottom should be something along the lines of:
• supplied from marcuswheelan.com.au
Nice to have
• A nice design with imagery/colours etc ... not just the text on a white background! Bright attractive colours preferred.
• I have uploaded my logo ... a roughly triangular image followed by my name etc. The triangular logo image could be used somewhere on the card and this logo can be interchangeable for other clinics who purchase the card.
• **Please note that I don't want my name to be included as part of the logo on the card ... just use the triangular image on the side of the logo without the following name**
• Also, the colouring of the card does not have to reflect my logo colours as I am anticipating interchanging this logo with other logos if other clinics choose to adopt the card. I am interested to see other, more generic, colour choices as well as my logo colours

```html
<!DOCTYPE html>
<html lang="en">
<head>
<meta charset="utf-8">
<title>Weight Loss Surgery Restaurant Card</title>
<link rel="stylesheet" href="https://fonts.googleapis.com/css2?family=Lato:wght@400;700&family=Cinzel:wght@400&display=swap">
<style>
  :root {
    --backdrop: #e6e8e8;
    --teal: #169487;
    --teal-deep: #0f7d73;
    --white: #ffffff;
    --ink: #2a2a2a;
    --grey-light: #f2f2f2;
    --grey-mid: #b9b9b9;
    --tagline: #7a7a7a;
  }
  * { margin: 0; padding: 0; box-sizing: border-box; }
  html, body {
    width: 1200px; height: 782px; overflow: hidden;
    background: var(--backdrop);
  }
  .stage {
    width: 1200px; height: 782px;
    display: flex; align-items: center; justify-content: center; gap: 40px;
  }
  .card {
    position: relative;
    width: 540px; height: 324px;
    box-shadow: 0 6px 18px rgba(0,0,0,0.18);
    overflow: hidden;
  }

  /* Details side */
  .card--details { background: var(--white); }
  .clinic-mark {
    position: absolute; top: 60px; right: 34px;
    display: flex; align-items: center; gap: 10px;
  }
  .clinic-mark__square {
    width: 34px; height: 34px; background: var(--teal);
  }
  .clinic-mark__name {
    font-family: "Lato", sans-serif; font-weight: 400;
    font-size: 27px; letter-spacing: 1px; color: var(--teal);
    line-height: 1;
  }
  .clinic-mark__tagline {
    font-family: "Lato", sans-serif; font-size: 8.5px;
    letter-spacing: 1.2px; text-transform: uppercase;
    color: var(--tagline); margin-top: 4px;
  }
  .fields {
    position: absolute; left: 34px; top: 44px;
    list-style: none;
    font-family: "Lato", sans-serif; font-size: 16px; color: var(--ink);
    line-height: 27px;
  }
  .supplier {
    position: absolute; left: 34px; top: 222px;
    font-family: "Lato", sans-serif; font-size: 16px; color: var(--ink);
    display: flex; align-items: baseline; gap: 10px;
  }
  .supplier__url {
    font-family: "Cinzel", serif; font-size: 18px; color: var(--teal);
    letter-spacing: 0.5px;
  }
  .card__bands { position: absolute; left: 0; bottom: 0; }

  /* Message side */
  .card--message {
    background: linear-gradient(160deg, var(--teal) 0%, var(--teal-deep) 100%);
  }
  .message {
    list-style: none;
    position: absolute; left: 44px; top: 44px; right: 36px;
    font-family: "Lato", sans-serif; font-size: 13.5px;
    text-transform: uppercase; color: var(--white);
    line-height: 19px; letter-spacing: 0.4px;
  }
  .message li { position: relative; padding-left: 14px; }
  .message li::before {
    content: ""; position: absolute; left: 0; top: 6px;
    width: 7px; height: 7px; border-radius: 50%; background: var(--white);
  }
</style>
</head>
<body>
<main class="stage">

  <section class="card card--details" aria-label="Patient details side">
    <div class="clinic-mark">
      <span class="clinic-mark__square" aria-hidden="true"></span>
      <div>
        <div class="clinic-mark__name">Marcus Wheelan</div>
        <div class="clinic-mark__tagline">General, Upper GI &amp; Bariatric Surgeon</div>
      </div>
    </div>
    <ul class="fields">
      <li>Name:</li>
      <li>Procedure performed:</li>
      <li>Date of procedure (month/year):</li>
      <li>Treating Clinic Name:</li>
      <li>Treating Clinic Signature:</li>
    </ul>
    <p class="supplier">PURCHASED THROUGH <span class="supplier__url">www.marcuswheelan.com.au</span></p>
    <svg class="card__bands" width="540" height="70" viewBox="0 0 540 70" aria-hidden="true">
      <defs>
        <linearGradient id="greyBand" x1="0" y1="0" x2="0" y2="1">
          <stop offset="0" stop-color="var(--grey-light)"/>
          <stop offset="1" stop-color="var(--grey-mid)"/>
        </linearGradient>
      </defs>
      <polygon points="0,44 250,44 238,70 0,70" fill="var(--teal)"/>
      <polygon points="258,18 540,18 540,70 236,70" fill="url(#greyBand)"/>
    </svg>
  </section>

  <section class="card card--message" aria-label="Restaurant message side">
    <ul class="message">
      <li>The individual bearing this card has undergone weight loss surgery.</li>
      <li>Around 500,000 of these procedures are performed around the world every year.</li>
      <li>This surgery restricts portion sizes to between half and one cup of food at a time.</li>
      <li>Please give consideration to allowing smaller portions of your regular meals to be ordered to reduce wastage and excess costs.</li>
      <li>Example: a half size portion priced at two thirds of usual cost.</li>
    </ul>
  </section>

</main>
</body>
</html>
```